Specialist Medical practice after professional trifold flyer design for patient information brochure

I am the Director of the Hollowbrook Clinic, a specialist medial and surgical practice in Australia. I am after a professional design of a patient information trifold flyer that can be used for web distribution or for commercial printing for upcoming educational event. The design would need to allow change of images and text to be used as template for future topics but have a common brand look across them. Colours would follow the logo, but primarily blue colours for the hollowbrook theme. The inside text needs to be clearly contrasted to the background for easy reading, as often elderly patients. The design would make use of curves or circles, but open for hexagonal, triangle square vector components. I have included an outline for the initial brochure and included images to include. Other stock background images can be used if they increase the impact of the design over included. A winning design is also one that could be modified to a 4 page bi-fold brochure

Target Market(s)

This will be provided to patients in GP practices, podiatry clinics, radiological practices. Aimed at patients to read and be compelled to look to site or get consultation with me

Industry/Entity Type

Medical

Font styles to use
Serif
Sans Serif

Colors
33a6d7
0355a3
86cfc6
cedeed
0292cd
85cae6

Requirements
Must have
• The front cover needs to engage the patient to pick up and read- yes I have a painful ankle and want to find out more. the goal for the inside is to provide the options but be able to direct to website for more info - website currently undergoing upgrade. After professional modern look. Not bright contrasting colours like many advertising brochures. Needs to able to have images and text changed but following same look to create new topics
Nice to have
• The focus is a Tri-fold brochure. Nice to be able to modify to bifold. A winning design would even offer both, or submit separate bifold and trifold. I am open to different versions of similar look. (eg option of brochure with curved elements, triangular or square, or hexagonal.
Should not have
• To many contrasting colours. Text must be easily read on background, either white or coloured background texture with transparency

```html
<!DOCTYPE html>
<html lang="en">
<head>
<meta charset="utf-8">
<title>Hollowbrook Clinic – Ankle Fusion Surgery Trifold</title>
<link rel="stylesheet" href="https://fonts.googleapis.com/css2?family=Roboto+Condensed:wght@700&family=Open+Sans:wght@400;600;700&display=swap">
<style>
:root{
  --blue-deep:#0355a3;
  --blue:#0292cd;
  --blue-sky:#33a6d7;
  --blue-soft:#85cae6;
  --blue-pale:#cedeed;
  --ink:#2d3a45;
  --white:#ffffff;
  --backdrop:#e8ecf0;
}
*{margin:0;padding:0;box-sizing:border-box}
html,body{width:1078px;height:1200px;overflow:hidden;background:var(--backdrop)}
body{position:relative;font-family:"Open Sans",Arial,sans-serif;color:var(--ink)}
.spread{position:absolute;left:44px;width:990px;height:560px;overflow:hidden;background:var(--white);box-shadow:0 4px 14px rgba(0,0,0,.18)}
.spread--inside{top:40px}
.spread--outside{top:620px}
.spread svg.shapes{position:absolute;inset:0;width:990px;height:560px}
.abs{position:absolute}
/* inside */
.arthritis-title{left:30px;top:22px;font-family:"Roboto Condensed",sans-serif;font-size:24px;color:var(--blue-deep);letter-spacing:.3px}
.tick-list{list-style:none}
.tick-list li{position:relative;padding-left:13px;margin-bottom:10px;font-size:9px;line-height:1.35}
.tick-list li::before{content:"";position:absolute;left:1px;top:2px;width:4px;height:7px;border:solid var(--blue-deep);border-width:0 2px 2px 0;transform:rotate(45deg)}
.arthritis-list{left:30px;top:62px;width:225px}
.arthritis-list li:nth-child(3){width:190px}
.arthritis-list li:nth-child(4){width:130px}
.fusion-title{right:350px;top:246px;text-align:right;font-family:"Roboto Condensed",sans-serif;font-size:44px;line-height:42px;color:var(--blue-deep)}
.fusion-body{left:346px;top:392px;width:298px;font-size:8.2px;line-height:1.45;text-align:justify;text-align-last:right}
.fusion-body p{margin-bottom:8px}
.fusion-detail{left:680px;top:36px;width:290px;color:var(--white);font-size:9px;line-height:1.45}
.more-info{left:680px;top:208px;width:290px;font-size:9px;line-height:1.4}
.more-info a{display:block;margin-top:6px;color:var(--blue-deep);font-weight:700;text-decoration:none}
/* outside */
.doctor-name{left:26px;top:24px;font-size:19px;font-weight:600;color:var(--blue-deep)}
.doctor-quals{left:26px;top:52px;font-size:8px;font-weight:600}
.doctor-bio{left:26px;top:68px;width:262px;font-size:8px;line-height:1.4}
.conditions-pill{left:20px;top:150px;padding:4px 12px;background:var(--blue);color:var(--white);border-radius:14px;font-size:15px;font-weight:600}
.conditions-intro{left:26px;top:188px;width:262px;font-size:8px;line-height:1.4}
.conditions-list{left:26px;top:216px;width:262px}
.conditions-list li{font-size:7.8px;margin-bottom:5px;color:var(--blue-deep);font-weight:600}
.contact{left:330px;width:330px;text-align:center;color:var(--white)}
.clinic-mark{top:348px;font-size:16px;font-weight:700;letter-spacing:1px}
.locations{top:382px;font-size:17px;font-weight:600}
.address{top:414px;font-size:8.5px;line-height:1.4;padding:0 40px}
.phones{top:450px;font-size:19px;font-weight:700;line-height:1.35}
.web-lines{top:508px;font-size:8.5px;line-height:1.5}
.cover-brand{left:660px;top:410px;width:330px;text-align:center}
.cover-brand .name{font-size:24px;font-weight:700;color:var(--blue-deep);letter-spacing:1px;display:inline-flex;align-items:center;gap:8px}
.cover-brand .name::before{content:"";width:14px;height:14px;border-radius:50%;background:var(--blue)}
.cover-brand .tag{font-size:8.5px;color:var(--blue-sky);letter-spacing:1.5px;margin-top:2px}
.cover-lead{left:660px;top:474px;width:330px;text-align:center;font-size:10.5px;line-height:1.35}
.cover-url{left:660px;top:536px;width:330px;text-align:center;font-size:7.5px;color:var(--blue-deep);letter-spacing:1px;font-weight:600}
</style>
</head>
<body>

<section class="spread spread--inside">
  <svg class="shapes" viewBox="0 0 990 560">
    <defs>
      <linearGradient id="g-xray-hands" x1="0" y1="0" x2="1" y2="1"><stop offset="0" stop-color="#0a6cbf"/><stop offset=".5" stop-color="#1aa2df"/><stop offset="1" stop-color="#5fcbef"/></linearGradient>
      <radialGradient id="g-xray" cx=".5" cy=".5" r=".7"><stop offset="0" stop-color="#bfc3c6"/><stop offset=".6" stop-color="#5b5f63"/><stop offset="1" stop-color="#1d1f21"/></radialGradient>
      <clipPath id="clip-p1"><rect x="0" y="0" width="330" height="560"/></clipPath>
      <clipPath id="clip-p3"><rect x="660" y="0" width="330" height="560"/></clipPath>
    </defs>
    <rect x="0" y="0" width="660" height="420" fill="url(#g-xray-hands)" role="img" aria-label="Hands holding a foot x-ray film"/>
    <rect x="0" y="330" width="330" height="230" fill="url(#g-xray)" role="img" aria-label="Side x-ray of an arthritic ankle"/>
    <g clip-path="url(#clip-p1)">
      <circle cx="70" cy="130" r="282" fill="none" stroke="var(--blue)" stroke-width="16"/>
      <circle cx="70" cy="130" r="270" fill="var(--white)"/>
    </g>
    <path d="M330 560 L330 440 C380 320 500 240 660 222 L660 560 Z" fill="var(--white)"/>
    <path d="M330 425 C380 306 500 226 660 208" fill="none" stroke="var(--blue-deep)" stroke-width="6"/>
    <g clip-path="url(#clip-p3)">
      <rect x="660" y="0" width="330" height="560" fill="var(--white)"/>
      <rect x="660" y="0" width="330" height="190" fill="var(--blue)"/>
      <rect x="660" y="190" width="330" height="7" fill="var(--blue-deep)"/>
      <circle cx="975" cy="505" r="232" fill="var(--blue)"/>
      <circle cx="975" cy="505" r="212" fill="url(#g-xray)" role="img" aria-label="X-ray of an ankle fused with plate and screws"/>
    </g>
    <rect x="0" y="552" width="990" height="8" fill="var(--blue-deep)"/>
    <line x1="330" y1="0" x2="330" y2="560" stroke="rgba(0,0,0,.08)"/>
    <line x1="660" y1="0" x2="660" y2="560" stroke="rgba(0,0,0,.08)"/>
  </svg>

  <h2 class="abs arthritis-title">ANKLE ARTHRITIS</h2>
  <ul class="abs tick-list arthritis-list">
    <li>Ankle arthritis is a painful condition where there is loss of cartilage from the ankle joint surface. Although not as common as knee or hip arthritis, pain can be debilitating affecting quality of life.</li>
    <li>Arthritis of the joint can be caused by trauma to the joint such as fracture or recurrent instability or secondary from inflammatory conditions such as rheumatoid arthritis.</li>
    <li>Pain from the joint will occur with activity causing a limp, limiting walking speed and distance. Often there is swelling of the joint with progressive loss of motion.</li>
    <li>Diagnosis is made with examination of the ankle and weight bearing x-rays showing loss of joint space.</li>
  </ul>

  <h1 class="abs fusion-title">ANKLE<br>FUSION<br>SURGERY</h1>
  <div class="abs fusion-body">
    <p>When pain medication, activity modification and shoe wear modification is no longer effective to control the pain then it is worthwhile discussing with your GP for referral to Dr Marcus Ellery for an opinion on further treatment. As an Orthopaedic Foot and Ankle surgeon, he will be able to assess your conditions and give advice on the best options for your treatment.</p>
    <p>The decision on the best option is based on your age, activity level, existing medical problems, previous ankle treatment and your expected outcome from treatment. In the situation of end stage arthritis options consist of either Ankle fusion or Total Ankle replacement.</p>
  </div>

  <p class="abs fusion-detail">This operation aims to stiffen the ankle joint by fusing the tibia and talus together in the optimal position for function. The common thought is that there will be no movement of the foot, and the patient will walk with a limp. The fusion only occurs at the ankle joint, leaving motion available to the surrounding joints. Although there is decreased motion, you will walk more normally after a fusion without a limp as the pain to the joint is removed.</p>
  <p class="abs more-info">For more information on ankle fusion, risks and recovery visit our website:<a href="#">www.hollowbrookclinic.com.au/Ankle-Fusion</a></p>
</section>

<section class="spread spread--outside">
  <svg class="shapes" viewBox="0 0 990 560">
    <defs>
      <linearGradient id="g-pale" x1="0" y1="0" x2="0" y2="1"><stop offset="0" stop-color="#f4f8fb"/><stop offset="1" stop-color="#d4e6f0"/></linearGradient>
      <linearGradient id="g-portrait" x1="0" y1="0" x2="0" y2="1"><stop offset="0" stop-color="#c9d6de"/><stop offset="1" stop-color="#2a3340"/></linearGradient>
      <linearGradient id="g-coast" x1="0" y1="0" x2="0" y2="1"><stop offset="0" stop-color="#b9d7e6"/><stop offset=".35" stop-color="#3f7a4e"/><stop offset=".6" stop-color="#4a9aa0"/><stop offset="1" stop-color="#6f8a3c"/></linearGradient>
      <linearGradient id="g-runner" x1="0" y1="0" x2="1" y2="1"><stop offset="0" stop-color="#f3e2c4"/><stop offset=".5" stop-color="#d9b37d"/><stop offset="1" stop-color="#9b8b55"/></linearGradient>
      <clipPath id="clip-o3"><rect x="660" y="0" width="330" height="560"/></clipPath>
    </defs>
    <rect x="0" y="0" width="330" height="560" fill="url(#g-pale)"/>
    <rect x="40" y="370" width="230" height="190" rx="4" fill="url(#g-portrait)" role="img" aria-label="Portrait of Dr Marcus Ellery in a suit"/>
    <rect x="330" y="0" width="330" height="560" fill="url(#g-coast)" role="img" aria-label="Coastal headland and beach landscape"/>
    <rect x="330" y="330" width="330" height="230" fill="rgba(0,40,60,.28)"/>
    <g clip-path="url(#clip-o3)">
      <rect x="660" y="0" width="330" height="560" fill="var(--white)"/>
      <circle cx="840" cy="150" r="236" fill="var(--blue)"/>
      <circle cx="840" cy="150" r="214" fill="url(#g-runner)" role="img" aria-label="Runner holding a painful ankle outdoors"/>
      <path d="M650 140 A190 190 0 0 1 780 -30" fill="none" stroke="var(--blue-soft)" stroke-width="8" opacity=".8"/>
    </g>
    <line x1="330" y1="0" x2="330" y2="560" stroke="rgba(0,0,0,.08)"/>
    <line x1="660" y1="0" x2="660" y2="560" stroke="rgba(0,0,0,.08)"/>
  </svg>

  <h2 class="abs doctor-name">Dr Marcus Ellery</h2>
  <p class="abs doctor-quals">MBBS (EUA), FRACS (Ortho), FA (Ortho)</p>
  <p class="abs doctor-bio">Dr Marcus Ellery is an Australian trained Orthopaedic Surgeon who has a primary focus in the treatment of conditions of the foot and ankle. He has completed post fellowship training in Foot and Ankle surgery both locally and internationally, and continues to update himself in the latest techniques.</p>
  <h3 class="abs conditions-pill">Conditions treated</h3>
  <p class="abs conditions-intro">Dr Ellery provides assessment and treatment of all foot and ankle conditions. He has special interest in the following:</p>
  <ul class="abs tick-list conditions-list">
    <li>Minimally invasive treatment for bunions and toe deformities.</li>
    <li>Joint sparing procedures for arthritis or deformity, including the Flexia implant.</li>
    <li>Joint fusion procedures for arthritis of the feet and ankle Sports injuries and tendinopathies.</li>
    <li>Total ankle replacement and deformity correction of the foot and ankle.</li>
  </ul>

  <p class="abs contact clinic-mark">HOLLOWBROOK CLINIC</p>
  <p class="abs contact locations">
    <svg width="12" height="16" viewBox="0 0 12 16" aria-hidden="true" style="vertical-align:-2px"><path d="M6 0a6 6 0 0 1 6 6c0 4-6 10-6 10S0 10 0 6a6 6 0 0 1 6-6z" fill="#fff"/><circle cx="6" cy="6" r="2.2" fill="#3f7a4e"/></svg>
    Locations</p>
  <p class="abs contact address">Suite 12, Level 3 Harbourside Private Hospital 48 Marina St Eastport NSW 9 Ridge Road Westvale NSW</p>
  <p class="abs contact phones">
    <svg width="13" height="15" viewBox="0 0 13 15" aria-hidden="true"><rect x="0" y="0" width="13" height="15" rx="2" fill="#fff"/><path d="M4 3c-1 1 0 5 4 8l1.5-1.5L8 8 7 9C6 8 5 7 5 5.8l1-.8L5 3z" fill="#3f7a4e"/></svg>
    (02) 4000 1234<br>
    <svg width="13" height="15" viewBox="0 0 13 15" aria-hidden="true"><rect x="0" y="4" width="13" height="11" rx="1" fill="#fff"/><rect x="3" y="0" width="7" height="5" fill="#fff"/></svg>
    (02) 4000 5678</p>
  <p class="abs contact web-lines">www.hollowbrookclinic.com.au<br>info@hollowbrookclinic.com.au</p>

  <div class="abs cover-brand">
    <div class="name">HOLLOWBROOK CLINIC</div>
    <div class="tag">MEDICAL &amp; SURGICAL SPECIALISTS</div>
  </div>
  <p class="abs cover-lead">My Painful Ankle Solutions for<br>Ankle Arthritis Dr Marcus Ellery<br>Orthopaedic Foot and Ankle Surgeon</p>
  <p class="abs cover-url">www.hollowbrookclinic.com.au</p>
</section>

</body>
</html>
```